Architectural Design Brochure

I need you to design 5 pages (they will be used as templates which I can then edit later).

Please design 5 pages - copy the example pdf provided as reference (Morrow Fold). Please copy pages 1,3,5,6,7 from the example provided. But make the style match my unique brand. I want the layout to be similar to the example but still must be unique - use my logo and brand style blue, white, silver and grey.

I must be able to edit the brochure myself after you have finished these 5 pages (to change text and images etc) so it must be given to me in suitable format which I can edit in (psd or gimp).

my website is www.plenwick.com.au
my logo is attached

Target Market(s)

Home Builders and Architects

Requirements
Must have
• I would like you to design it around my brand - white, blue, grey and silver.

Must do 5 pages, copy the layout as shown in the example Morrow Fold pdf - I need pages 1,3,5,6,7
Nice to have
• Unique stlye
same layout as example - pages 1,3,5,6,7
Should not have
• Should not be exactly same style / watermarks etc as example

```html
<!DOCTYPE html>
<html lang="en">
<head>
<meta charset="utf-8">
<title>MFD – A forward thinking company</title>
<link rel="stylesheet" href="https://fonts.googleapis.com/css2?family=Nothing+You+Could+Do&family=Source+Sans+3:wght@400;600;700&display=swap">
<style>
  :root {
    --sky-top: #4aaee2;
    --sky-mid: #3a7cc4;
    --navy-bottom: #2a347c;
    --white: #ffffff;
    --ice: #b5dcf5;
    --ice-soft: #a7cdee;
    --silver: #dfe6ee;
    --brand-orange: #f08a1c;
  }
  * { margin: 0; padding: 0; box-sizing: border-box; }
  html, body {
    width: 840px; height: 1200px; overflow: hidden;
    background: var(--navy-bottom);
  }
  .page {
    position: relative;
    width: 840px; height: 1200px;
    overflow: hidden;
    background: linear-gradient(180deg, var(--sky-top) 0%, var(--sky-mid) 45%, var(--navy-bottom) 100%);
    font-family: "Source Sans 3", "Myriad Pro", Arial, sans-serif;
    color: var(--white);
  }
  .headline {
    position: absolute; top: 168px; left: 0; width: 840px;
    text-align: center;
    font-family: "Nothing You Could Do", cursive;
    font-size: 62px; font-weight: 400; letter-spacing: 1px;
    color: var(--white);
  }
  .intro {
    position: absolute; top: 324px; left: 59px; width: 700px;
    font-size: 24px; line-height: 44px; font-weight: 400;
  }
  .services, .directors {
    position: absolute; left: 59px; width: 720px;
    font-size: 15.5px; line-height: 43px;
    color: var(--ice);
  }
  .services { top: 535px; }
  .directors { top: 752px; color: var(--ice-soft); }
  .signature {
    position: absolute; height: 84px; border-radius: 6px;
    background: linear-gradient(90deg, rgba(255,255,255,0.22), rgba(255,255,255,0.08));
  }
  .signature--left { left: 112px; top: 952px; width: 308px; }
  .signature--right { left: 476px; top: 952px; width: 182px; }
  .signatory {
    position: absolute; top: 1058px;
  }
  .signatory--left { left: 87px; }
  .signatory--right { left: 486px; }
  .signatory__line {
    width: 225px; height: 0;
    border-top: 3px dotted var(--silver);
  }
  .signatory__name {
    margin-top: 18px; font-size: 15.5px; color: var(--white);
  }
  .brand {
    position: absolute; top: 1140px; left: 0; width: 840px;
    display: flex; justify-content: center; align-items: center; gap: 10px;
  }
  .brand__mark {
    width: 26px; height: 26px; background: var(--silver); border-radius: 3px;
  }
  .brand__name {
    font-size: 28px; font-weight: 700; color: var(--brand-orange);
  }
</style>
</head>
<body>
<main class="page">
  <h1 class="headline">A forward thinking company</h1>

  <p class="intro">MFD is a unique Australian owned and operated outsource Design, Drafting and 3D Presentation firm. We provide a 7 day residential project turnaround . We service every state and every city, Australia-wide.</p>

  <p class="services">MFD is here to specifically service Builders, Property Developers, Architects and<br>Designers. We do this so your projects are our only priority, for your peace of mind.<br>Our key services are Design, Drafting, Documentation, 3D Presentations,<br>Multi-residential and Commercial projects.</p>

  <p class="directors">We are the founding directors of MFD a division of Morrow Fold Group Australia and<br>are responsible for the company’s forward direction and day-to-day operations,<br>ensuring your projects are delivered to our high standards and on time, everytime...</p>

  <div class="signature signature--left" role="img" aria-label="Handwritten signature of Calder Voss"></div>
  <div class="signature signature--right" role="img" aria-label="Handwritten signature of Imogen Voss"></div>

  <div class="signatory signatory--left">
    <div class="signatory__line"></div>
    <p class="signatory__name">Calder Voss</p>
  </div>
  <div class="signatory signatory--right">
    <div class="signatory__line"></div>
    <p class="signatory__name">Imogen Voss</p>
  </div>

  <div class="brand">
    <span class="brand__mark"></span>
    <span class="brand__name">Plenwick</span>
  </div>
</main>
</body>
</html>
```